Business Card Design Project

We need a Business Card for an Mechanical Engineering firm in Singapore. The design should be Modern & Technical looking, yet eye catching.

Our company deals in Cutting Tools & Machine Accessories for the Manufacturing Industries such as Oil & Gas, Aero Space, etc... For more information on our Company, you can either email me or view our website www.valtrion.com.sg.

We are trying to revamp our image to give our consumers a fresh new perspective to our company, so we welcome all ideas.

Industry/Entity Type

Business

Requirements
Must have
• Must incorporate New Company Logo into the card as shown in Uploaded file.

```html
<!DOCTYPE html>
<html lang="en">
<head>
<meta charset="utf-8">
<title>Valtrion Tools – Business Card</title>
<link href="https://fonts.googleapis.com/css2?family=Ubuntu:ital,wght@0,400;0,500;1,700&display=swap" rel="stylesheet">
<style>
  :root {
    --crimson: #9b1b37;
    --crimson-deep: #3d1221;
    --crimson-glow: #8a1c34;
    --ink: #2a2326;
    --paper: #ffffff;
    --backdrop: #ece9e6;
    --accent-dark: #3a1a22;
  }
  * { margin: 0; padding: 0; box-sizing: border-box; }
  html, body {
    width: 1200px; height: 900px; overflow: hidden;
    background: var(--backdrop);
    font-family: "Ubuntu", sans-serif;
  }
  .canvas { position: relative; width: 1200px; height: 900px; }

  .card {
    position: absolute; left: 280px; width: 640px; height: 390px;
    overflow: hidden;
    box-shadow: 0 6px 14px rgba(0,0,0,.25);
  }
  .card--front { top: 50px; background: var(--paper); }
  .card--back {
    top: 480px;
    background: radial-gradient(ellipse at 50% 45%, var(--crimson-glow) 0%, #5a1628 45%, var(--crimson-deep) 100%);
  }

  .card__band {
    position: absolute; left: 0; right: 0; bottom: 0; height: 17px;
    background: var(--crimson);
  }
  .card__band::before, .card__band::after {
    content: ""; position: absolute; top: 0; height: 17px; width: 21px;
  }
  .card__band::before { left: 562px; background: var(--accent-dark); }
  .card__band::after  { left: 583px; background: var(--paper); }

  .brand {
    position: absolute; display: flex; align-items: center; gap: 10px;
    font-weight: 500; letter-spacing: .04em; text-transform: uppercase;
  }
  .brand__dot { border-radius: 50%; background: var(--crimson); flex: none; }
  .card--front .brand { right: 36px; top: 100px; color: var(--crimson); font-size: 30px; }
  .card--front .brand__dot { width: 22px; height: 22px; }
  .card--back .brand {
    left: 0; right: 0; top: 165px; justify-content: center;
    color: var(--paper); font-size: 54px;
  }
  .card--back .brand__dot { width: 36px; height: 36px; background: #c03550; }

  .person { position: absolute; left: 54px; top: 158px; }
  .person__name { font-style: italic; font-weight: 700; font-size: 20px; color: var(--crimson); }
  .person__role { font-size: 17px; color: var(--ink); margin-top: 4px; }
  .person__rule {
    width: 286px; height: 1px; margin-top: 11px;
    background: linear-gradient(90deg, var(--crimson), rgba(155,27,55,0));
  }

  .contacts { position: absolute; left: 54px; top: 234px; list-style: none; color: var(--ink); font-size: 17.5px; }
  .contacts li { display: flex; align-items: flex-start; gap: 6px; line-height: 24px; }
  .contacts svg { width: 20px; height: 20px; margin-top: 2px; flex: none; }
</style>
</head>
<body>
<main class="canvas">

  <section class="card card--front" aria-label="Business card front">
    <div class="brand"><span class="brand__dot"></span>Valtrion Tools</div>

    <div class="person">
      <p class="person__name">Fname Lname</p>
      <p class="person__role">Company Position</p>
      <div class="person__rule"></div>
    </div>

    <ul class="contacts">
      <li>
        <svg viewBox="0 0 20 20" aria-hidden="true"><rect x="4" y="3" width="12" height="15" rx="1.5" fill="var(--crimson)"/><rect x="6" y="5" width="8" height="4" fill="#fff"/><g fill="#fff"><rect x="6" y="11" width="2" height="2"/><rect x="9" y="11" width="2" height="2"/><rect x="12" y="11" width="2" height="2"/><rect x="6" y="14" width="2" height="2"/><rect x="9" y="14" width="2" height="2"/><rect x="12" y="14" width="2" height="2"/></g></svg>
        <span>123-456-7890</span>
      </li>
      <li>
        <svg viewBox="0 0 20 20" aria-hidden="true"><rect x="2" y="5" width="16" height="11" fill="none" stroke="var(--crimson)" stroke-width="1.5"/><path d="M2 5l8 6 8-6M2 16l6-5M18 16l-6-5" fill="none" stroke="var(--crimson)" stroke-width="1.3"/></svg>
        <span>name@valtrion.com.sg</span>
      </li>
      <li>
        <svg viewBox="0 0 20 20" aria-hidden="true"><circle cx="10" cy="10" r="8" fill="none" stroke="var(--crimson)" stroke-width="1.6"/><ellipse cx="10" cy="10" rx="3.5" ry="8" fill="none" stroke="var(--crimson)" stroke-width="1.2"/><path d="M2 10h16M3.5 6h13M3.5 14h13" stroke="var(--crimson)" stroke-width="1.2"/></svg>
        <span>www.valtrion.com.sg</span>
      </li>
      <li>
        <svg viewBox="0 0 20 20" aria-hidden="true"><path d="M2 10l8-7 8 7" fill="none" stroke="var(--crimson)" stroke-width="1.8"/><path d="M4.5 9v8h11V9" fill="none" stroke="var(--crimson)" stroke-width="1.6"/><rect x="8.5" y="12" width="3" height="5" fill="var(--crimson)"/></svg>
        <span>27 Kallang Way #03-12, Meridian<br>Industrial Park, Singapore 349215</span>
      </li>
    </ul>

    <div class="card__band"></div>
  </section>

  <section class="card card--back" aria-label="Business card back">
    <div class="brand"><span class="brand__dot"></span>Valtrion Tools</div>
    <div class="card__band"></div>
  </section>

</main>
</body>
</html>
```